Tandle Repair - Handyman and Home Repair Services

I need a business card/letterhead logo for my new handyman service in my local area. I'm happy for a logo design to be done prior to business card design so it can be incorporated on to the card, for which I'd be happy to pay more for. I'd like it to be modern and not using the typical pictures of tools and cartoon characters in dungarees! I like the idea of tools but in a more modern way i.e subtle background images in different shades to main colour. I do like the american retro designs and those that show age and patina for example, having an image half old, half new in its appearance to represent the repairing of things. Colours in mind are 1950's retro colours, ie using grey with pastel greens, red and cream. I'd like to break the mould and the stigma thats attached to these jobs and make it more cool and up to date. I hope this will attract interior designers and more modern businesses to use my services.

This is the logo design I like and would be happy for this idea and colours:

http://toast-a-roam.co.uk/wp-content/uploads/2011/01/t-r_logo600px.png

```html
<!DOCTYPE html>
<html lang="en">
<head>
<meta charset="utf-8">
<title>Tandle Repair – Business Card</title>
<link rel="stylesheet" href="https://fonts.googleapis.com/css2?family=Cabin:wght@500;700&family=Kalam:wght@400&display=swap">
<style>
  :root {
    --stage: #e9e6e0;
    --card-dark: #2b2b2b;
    --card-mid: #3a3a3a;
    --card-edge: #1f1f1f;
    --pastel-green: #8cc63f;
    --cream: #f3dfa2;
    --cream-soft: #efe2b8;
  }
  * { box-sizing: border-box; margin: 0; padding: 0; }
  html, body {
    width: 1200px;
    height: 784px;
    overflow: hidden;
    background: var(--stage);
  }
  .canvas {
    position: relative;
    width: 1200px;
    height: 784px;
  }
  .card {
    position: absolute;
    width: 525px;
    height: 300px;
    border-radius: 4px;
    overflow: hidden;
    box-shadow: 0 6px 18px rgba(0,0,0,0.18);
  }
  .card--details { left: 70px; top: 110px; }
  .card--brand { left: 605px; top: 374px; }
  .card__texture {
    position: absolute;
    inset: 0;
    background: radial-gradient(ellipse at 40% 40%, var(--card-mid) 0%, var(--card-dark) 70%, var(--card-edge) 100%);
  }
  .card__content {
    position: relative;
    height: 100%;
    display: flex;
    flex-direction: column;
    align-items: center;
    font-family: "Cabin", "Helvetica Neue", Arial, sans-serif;
  }
  .card--details .card__content { padding-top: 30px; }
  .card--brand .card__content { justify-content: center; }

  .brand-lockup {
    display: flex;
    align-items: center;
    gap: 10px;
    color: var(--pastel-green);
    font-weight: 700;
  }
  .brand-lockup__dot {
    border-radius: 50%;
    background: var(--pastel-green);
    flex: none;
  }
  .brand-lockup--small { font-size: 24px; }
  .brand-lockup--small .brand-lockup__dot { width: 16px; height: 16px; }
  .brand-lockup--large { font-size: 50px; gap: 16px; }
  .brand-lockup--large .brand-lockup__dot { width: 34px; height: 34px; }

  .tagline {
    margin-top: 20px;
    font-family: "Kalam", "Comic Sans MS", cursive;
    font-size: 19px;
    color: var(--cream);
    letter-spacing: 0.3px;
  }
  .contact-name {
    margin-top: 18px;
    font-size: 27px;
    font-weight: 700;
    color: var(--pastel-green);
  }
  .contact-line {
    font-size: 20px;
    font-weight: 500;
    color: var(--cream-soft);
    line-height: 1.35;
  }
  .contact-line--phone { margin-top: 14px; }
</style>
</head>
<body>
<main class="canvas">
  <section class="card card--details">
    <div class="card__texture" role="img" aria-label="Charcoal card background with faint pattern of hand tools"></div>
    <div class="card__content">
      <div class="brand-lockup brand-lockup--small">
        <span class="brand-lockup__dot"></span>
        <span class="brand-lockup__name">Tandle Repair</span>
      </div>
      <p class="tagline">Handyman services from repair to install</p>
      <p class="contact-name">Martin Hale</p>
      <p class="contact-line contact-line--phone">07700 900418</p>
      <p class="contact-line">www.tandlerepair.co.uk</p>
    </div>
  </section>

  <section class="card card--brand">
    <div class="card__texture" role="img" aria-label="Charcoal card background with faint pattern of hand tools"></div>
    <div class="card__content">
      <div class="brand-lockup brand-lockup--large">
        <span class="brand-lockup__dot"></span>
        <span class="brand-lockup__name">Tandle Repair</span>
      </div>
    </div>
  </section>
</main>
</body>
</html>
```